Business card

would like a double sided business card made up with my logos provided.
Prefer card to have black background and to use the black logos, with matching blue writing for the text.
One side to just be the logo, (Try to use both the black logos)
the other side to have the logo and also my credentials/business information.

Covering all aspects of Carpentry and Building Services

Marcus Thelwin
Qualified Carpenter
Mob: 0417263985
Email: rkt.joinery@fernmail.example
ABN: 47 619 283 504

Industry/Entity Type

Business

Contact Information for Business Card

Marcus Thelwin
Qualified Carpenter
Mob: 0417263985
ABN: 47 619 283 504

Requirements
Must have
• Please try to use both the black logos and incorporate into the card.

```html
<!DOCTYPE html>
<html lang="en">
<head>
<meta charset="utf-8">
<title>RKT Joinery – Business Card</title>
<link href="https://fonts.googleapis.com/css2?family=Open+Sans:wght@400;600;700&display=swap" rel="stylesheet">
<style>
  :root {
    --backdrop: #a6a6a6;
    --wood-dark: #5a3312;
    --wood-mid: #9a5c22;
    --wood-light: #c8893e;
    --panel-dark: #1f1f1f;
    --panel-mid: #2b2b2b;
    --ink: #2e2e2e;
    --brand-blue: #1565b8;
    --paper: #ffffff;
    --faint: #ececec;
  }
  * { box-sizing: border-box; margin: 0; padding: 0; }
  html, body { width: 1200px; height: 900px; overflow: hidden; }
  body {
    background: var(--backdrop);
    font-family: "Open Sans", Arial, sans-serif;
    position: relative;
  }
  .card {
    position: absolute;
    top: 290px;
    width: 540px;
    height: 320px;
    border-radius: 24px;
    overflow: hidden;
    box-shadow: 0 10px 24px rgba(0,0,0,0.25);
  }
  .card--front { left: 40px; }
  .card--back { left: 620px; background: var(--paper); }

  .wood {
    background: linear-gradient(90deg, var(--wood-dark), var(--wood-mid) 20%, var(--wood-light) 45%, var(--wood-mid) 70%, var(--wood-dark));
  }
  .card--front .wood { position: absolute; inset: 0; }
  .front-panel {
    position: absolute;
    inset: 26px 24px;
    border-radius: 20px;
    background: linear-gradient(90deg, var(--panel-dark), var(--panel-mid) 50%, var(--panel-dark));
    display: flex;
    flex-direction: column;
    align-items: center;
    justify-content: center;
  }
  .front-name {
    color: var(--paper);
    font-weight: 400;
    font-size: 40px;
    letter-spacing: 6px;
    line-height: 1;
  }
  .front-tagline {
    margin-top: 10px;
    color: var(--brand-blue);
    font-size: 16px;
    letter-spacing: 1.5px;
  }

  .back-watermark {
    position: absolute;
    left: -10px;
    top: 120px;
    font-size: 150px;
    font-weight: 700;
    color: var(--faint);
    line-height: 1;
    letter-spacing: 4px;
  }
  .back-logo {
    position: absolute;
    left: 32px;
    top: 46px;
  }
  .back-name {
    font-size: 40px;
    font-weight: 400;
    color: var(--ink);
    letter-spacing: 1px;
    line-height: 1;
  }
  .back-tagline {
    margin-top: 4px;
    font-size: 11px;
    letter-spacing: 3px;
    color: var(--brand-blue);
    padding-left: 130px;
  }
  .name-band {
    position: absolute;
    left: 0; right: 0;
    top: 130px;
    height: 70px;
    background: var(--brand-blue);
    color: var(--paper);
    text-align: center;
    display: flex;
    flex-direction: column;
    justify-content: center;
  }
  .holder-name { font-size: 20px; font-weight: 600; line-height: 1.2; }
  .holder-role { font-size: 15px; line-height: 1.2; }
  .contact-list {
    position: absolute;
    right: 22px;
    top: 212px;
    list-style: none;
    text-align: right;
    color: var(--ink);
    font-size: 14px;
    line-height: 24px;
  }
  .contact-list li { display: flex; justify-content: flex-end; align-items: center; gap: 12px; }
  .contact-list svg { width: 14px; height: 12px; fill: var(--brand-blue); }
  .contact-list .abn { color: var(--brand-blue); font-size: 16px; padding-right: 26px; }
  .rule {
    position: absolute;
    left: 0; right: 0;
    top: 285px;
    height: 4px;
    background: var(--brand-blue);
  }
  .card--back .wood {
    position: absolute;
    left: 0; right: 0;
    top: 289px;
    bottom: 0;
  }
</style>
</head>
<body>
  <section class="card card--front">
    <div class="wood" role="img" aria-label="Timber grain border"></div>
    <div class="front-panel" role="img" aria-label="Dark stained timber boards">
      <span class="front-name">RKT JOINERY</span>
      <span class="front-tagline">CARPENTERS AND BUILDERS</span>
    </div>
  </section>

  <section class="card card--back">
    <div class="back-watermark" aria-hidden="true">RKT</div>
    <div class="back-logo">
      <div class="back-name">RKT JOINERY</div>
      <div class="back-tagline">CARPENTERS AND BUILDERS</div>
    </div>
    <div class="name-band">
      <span class="holder-name">Marcus Thelwin</span>
      <span class="holder-role">Qualified Carpenter</span>
    </div>
    <ul class="contact-list">
      <li>0417263985
        <svg viewBox="0 0 14 12" aria-hidden="true"><path d="M1 4c0-2 3-3 6-3s6 1 6 3v1h-3V3.5H4V5H1z M3 6h8l1 5H2z"/></svg>
      </li>
      <li>rkt.joinery@fernmail.example
        <svg viewBox="0 0 14 12" aria-hidden="true"><path d="M1 2h12v8H1z M1 2l6 5 6-5" stroke="#fff" stroke-width="1"/></svg>
      </li>
      <li class="abn">ABN: 47 619 283 504</li>
    </ul>
    <div class="rule"></div>
    <div class="wood" role="img" aria-label="Timber grain strip"></div>
  </section>
</body>
</html>
```